New Label Design Project

DetailHi, we are a small Farm growing and selling fresh and dehydrated exotic vegetables to exotic market and ethnic restaurants. We plan to make changes our packaging by using clamshell instead of bags. This is why we send you this project. Our main Target Market are Jamaican, Haitian, Egyptian and Turkish restaurant. Small supermarket Markets like Zentrol, Marquesino, Tollgate Food Market, Kelby food Market.... I sale to reseller in some farmers Market in Florida and Massachusetts. Then we have some direct customers they pick it at the farm stand. We don't have any online presence, my apologies... We are still working on that... We send you different logo. We are still working on the sizes of the clamshell. s for my new Label Design Project will be added soon.

```html
<!DOCTYPE html>
<html lang="en">
<head>
<meta charset="utf-8">
<title>Linden Brook Farm – Exotic Dried Mixed Vegetables Label</title>
<link href="https://fonts.googleapis.com/css2?family=League+Spartan:wght@400;500;800&display=swap" rel="stylesheet">
<style>
  :root {
    --bg: #ebebeb;
    --brand-blue: #2272cc;
    --art-blue: #2a78d0;
    --sun-yellow: #ffd200;
    --leaf-green: #3eaa35;
    --white: #ffffff;
  }
  * { margin: 0; padding: 0; box-sizing: border-box; }
  html, body {
    width: 1200px; height: 600px; overflow: hidden;
    background: var(--bg);
    font-family: "League Spartan", "Helvetica Neue", Arial, sans-serif;
  }
  .canvas { position: relative; width: 1200px; height: 600px; }

  /* Lid label */
  .label {
    position: absolute; left: 99px; top: 75px;
    width: 402px; height: 229px;
    border-radius: 30px; overflow: hidden;
    background: var(--white);
    display: flex;
  }
  .label__side {
    width: 166px; height: 100%;
    background: var(--brand-blue);
    position: relative; color: var(--white);
  }
  .label__art {
    position: absolute; left: 8px; top: 8px;
    width: 150px; height: 150px;
    border-radius: 10px;
    background: var(--art-blue);
  }
  .label__claims {
    position: absolute; left: 16px; top: 168px;
    font-size: 10.5px; font-weight: 400; line-height: 12px;
    letter-spacing: 0.1px; white-space: nowrap;
  }
  .label__weight {
    position: absolute; left: 0; width: 100%; top: 205px;
    text-align: center; font-size: 11px; font-weight: 500;
  }
  .label__main { position: relative; flex: 1; }
  .label__rule {
    position: absolute; left: 16px; top: 28px;
    width: 135px; height: 6px; background: var(--leaf-green);
  }
  .title {
    position: absolute; left: 15px; top: 38px;
    font-weight: 800; line-height: 1;
    text-transform: uppercase;
  }
  .title__kicker { display: block; font-size: 36px; color: var(--sun-yellow); letter-spacing: -0.5px; }
  .title__line { display: block; font-size: 57px; color: var(--brand-blue); letter-spacing: -1px; line-height: 48px; margin-top: 2px; }
  .title__noun { display: block; font-size: 27px; color: var(--leaf-green); letter-spacing: -0.3px; margin-top: 2px; }
  .label__organic {
    position: absolute; left: 16px; top: 198px;
    font-size: 15px; font-weight: 500; color: var(--leaf-green);
  }
  .brand-mark {
    position: absolute; right: 12px; top: 24px;
    width: 60px; text-align: center;
    color: var(--leaf-green);
  }
  .brand-mark__dot {
    width: 30px; height: 30px; margin: 0 auto 5px;
    border: 2px solid var(--leaf-green); border-radius: 50%;
  }
  .brand-mark__name { font-size: 9px; font-weight: 500; line-height: 10px; text-transform: uppercase; }

  /* Seal sticker */
  .seal {
    position: absolute; left: 209px; top: 344px;
    width: 182px; height: 182px; border-radius: 50%;
    background: var(--brand-blue);
    display: flex; flex-direction: column; align-items: center; justify-content: center;
    color: var(--white);
  }
  .seal__dot {
    width: 62px; height: 62px; border: 2px solid var(--white); border-radius: 50%;
    margin-bottom: 14px;
  }
  .seal__name { font-size: 17px; font-weight: 500; text-transform: uppercase; letter-spacing: 0.3px; }
</style>
</head>
<body>
<main class="canvas">
  <section class="label" aria-label="Lid label">
    <div class="label__side">
      <div class="label__art" role="img" aria-label="Line illustrations of vegetables: tomato, onion, eggplant, turnip, carrot, broccoli, leafy greens, pepper and bitter melon"></div>
      <p class="label__claims">• NON GMO &nbsp;• LOW CALORIE<br>• LOW CARB &nbsp;• GLUTEN FREE</p>
      <p class="label__weight">60 g</p>
    </div>
    <div class="label__main">
      <div class="label__rule"></div>
      <h1 class="title">
        <span class="title__kicker">Exotic</span>
        <span class="title__line">Dried</span>
        <span class="title__line">Mixed</span>
        <span class="title__noun">Vegetables</span>
      </h1>
      <p class="label__organic">100% ORGANIC</p>
      <div class="brand-mark">
        <div class="brand-mark__dot"></div>
        <p class="brand-mark__name">Linden Brook Farm</p>
      </div>
    </div>
  </section>

  <section class="seal" aria-label="Seal sticker">
    <div class="seal__dot"></div>
    <p class="seal__name">Linden Brook Farm</p>
  </section>
</main>
</body>
</html>
```